Watch brand needs new business cards

Kestrel Timepiece Company are looking for a new business card design incorporating our logo and brand colours as per our website.

Design should be 90x55mm with 3mm print margin from edges and 3mm external bleed.

Card should be double sided, e.g. logo one side, personal details on the other.

Logo will be provided as a vector.

The card must be able to show:
- Staff name
- Position
- Office Address
- Email
- Telephone number
- Website address

Final work must be provided in an editable format to allow us to add staff details (e.g. an AI or PSD file).

```html
<!DOCTYPE html>
<html lang="en">
<head>
<meta charset="utf-8">
<title>Kestrel Timepiece Company – Business Cards</title>
<link rel="stylesheet" href="https://fonts.googleapis.com/css2?family=Open+Sans:wght@400;600;700&display=swap">
<style>
  :root {
    --backdrop: #dedad8;
    --card: #f1f0ef;
    --ink: #0a0a0a;
    --paper: #ffffff;
  }
  * { box-sizing: border-box; margin: 0; padding: 0; }
  html, body { width: 1200px; height: 900px; overflow: hidden; }
  body {
    background: var(--backdrop);
    font-family: "Open Sans", Arial, sans-serif;
    position: relative;
  }
  .card {
    position: absolute;
    background: var(--card);
    box-shadow: 0 6px 18px rgba(0,0,0,0.12);
  }
  .card--front { left: 190px; top: 70px; width: 570px; height: 352px; }
  .card--back  { left: 518px; top: 472px; width: 560px; height: 340px; }

  .band {
    position: absolute;
    background: var(--ink);
  }
  .card--front .band { left: 5px; top: 48px; right: 0; height: 277px; border-radius: 138px 0 0 138px; }
  .card--back  .band { left: 0; top: 46px; right: 0; height: 270px; border-radius: 0 135px 135px 0; }

  .emblem {
    position: absolute;
    width: 246px; height: 246px;
    border-radius: 50%;
    background: var(--paper);
    border: 10px solid var(--ink);
    display: flex; align-items: center; justify-content: center;
    text-align: center;
    color: var(--ink);
    font-weight: 700;
    font-size: 20px;
    line-height: 1.25;
    letter-spacing: 1px;
    text-transform: uppercase;
    padding: 30px;
  }
  .card--front .emblem { left: 18px; top: 64px; }
  .card--back  .emblem { right: 18px; top: 58px; }

  .details {
    position: absolute;
    right: 24px; top: 84px;
    text-align: right;
    color: var(--paper);
  }
  .details__name { font-size: 19px; font-weight: 700; line-height: 1.2; }
  .details__role { font-size: 14px; line-height: 1.3; }
  .details__address { margin-top: 36px; font-size: 14px; line-height: 1.5; }
  .details__contacts { margin-top: 16px; list-style: none; font-size: 14px; line-height: 1.5; }
  .details__contacts li { display: flex; justify-content: flex-end; align-items: center; gap: 8px; }
  .details__contacts svg { width: 11px; height: 11px; fill: var(--paper); }

  .wordmark {
    position: absolute;
    left: 20px; top: 234px;
    width: 270px;
    text-align: center;
    color: var(--paper);
    font-weight: 600;
    font-size: 24px;
    letter-spacing: 1px;
    line-height: 1.15;
    text-transform: uppercase;
  }
</style>
</head>
<body>
  <section class="card card--front" aria-label="Business card, details side">
    <div class="band"></div>
    <div class="emblem">Kestrel Timepiece Company</div>
    <div class="details">
      <p class="details__name">Daniel Reeve</p>
      <p class="details__role">Position</p>
      <p class="details__address">12345, Address Goes Here<br>Country Name, 123456.</p>
      <ul class="details__contacts">
        <li>044-987 654 321
          <svg viewBox="0 0 24 24" aria-hidden="true"><path d="M6.6 10.8a15.1 15.1 0 0 0 6.6 6.6l2.2-2.2a1 1 0 0 1 1-.25 11.4 11.4 0 0 0 3.6.57 1 1 0 0 1 1 1V20a1 1 0 0 1-1 1A17 17 0 0 1 3 4a1 1 0 0 1 1-1h3.5a1 1 0 0 1 1 1c0 1.25.2 2.45.57 3.57a1 1 0 0 1-.25 1z"/></svg>
        </li>
        <li>hello@kestrelco.com
          <svg viewBox="0 0 24 24" aria-hidden="true"><path d="M2 5h20v14H2zM4 7v.5l8 5 8-5V7l-8 5z"/></svg>
        </li>
        <li>www.kestrelco.com
          <svg viewBox="0 0 24 24" aria-hidden="true"><circle cx="12" cy="12" r="10"/></svg>
        </li>
      </ul>
    </div>
  </section>

  <section class="card card--back" aria-label="Business card, brand side">
    <div class="band"></div>
    <p class="wordmark">Kestrel Timepiece Company</p>
    <div class="emblem">Kestrel Timepiece Company</div>
  </section>
</body>
</html>
```